SkyRavelin Unique Gift Certificate

We need a unique, luxury gift certificate created for our online company (SkyRavelin). We are looking for something out of the ordinary, ie. do not want it to look like a 'normal' gift certificate. Please visit our website to gain a feel for our company (skyravelin.com.au). The dimensions are 148x148mm. We need our logo, website details, to, from, description, code, exp date included. The certificate will be printed on wood veneer so watermarks will not work. We want it to be clean and minimalistic.

Industry/Entity Type

It Company

```html
<!DOCTYPE html>
<html lang="en">
<head>
<meta charset="UTF-8">
<title>SkyRavelin Gift Certificate</title>
<link href="https://fonts.googleapis.com/css2?family=Arimo:wght@400&family=Montserrat:wght@400&display=swap" rel="stylesheet">
<style>
  :root {
    --paper: #ffffff;
    --ink: #1f1f1f;
    --rule: #4a4a4a;
    --brand: #1b8dbf;
  }
  * { margin: 0; padding: 0; box-sizing: border-box; }
  html, body {
    width: 1200px;
    height: 1200px;
    overflow: hidden;
    background: var(--paper);
  }
  .certificate {
    position: relative;
    width: 1200px;
    height: 1200px;
    background: var(--paper);
  }
  .brand-block {
    position: absolute;
    top: 340px;
    left: 0;
    width: 100%;
    text-align: center;
  }
  .brand-name {
    font-family: "Montserrat", sans-serif;
    font-weight: 400;
    font-size: 42px;
    letter-spacing: 0.5px;
    color: var(--brand);
    line-height: 1;
  }
  .brand-tagline {
    margin-top: 16px;
    font-family: "Montserrat", sans-serif;
    font-weight: 400;
    font-size: 13px;
    letter-spacing: 1px;
    color: var(--ink);
    line-height: 1;
  }
  .fields {
    position: absolute;
    left: 177px;
    width: 866px;
    top: 510px;
  }
  .field {
    display: flex;
    align-items: flex-end;
    height: 87px;
    font-family: "Arimo", sans-serif;
    font-size: 30px;
    letter-spacing: -0.8px;
    color: var(--ink);
  }
  .field-label {
    white-space: nowrap;
    line-height: 1;
  }
  .field-line {
    flex: 1;
    border-bottom: 2px solid var(--rule);
    margin-bottom: 2px;
  }
  .site-address {
    position: absolute;
    left: 0;
    width: 100%;
    top: 1132px;
    text-align: center;
    font-family: "Montserrat", sans-serif;
    font-weight: 400;
    font-size: 32px;
    color: var(--brand);
    letter-spacing: 0.3px;
    line-height: 1.2;
  }
</style>
</head>
<body>
  <main class="certificate">
    <header class="brand-block">
      <div class="brand-name">SkyRavelin</div>
      <div class="brand-tagline">Explore · Gift · Share</div>
    </header>

    <section class="fields">
      <div class="field"><span class="field-label">To:</span><span class="field-line"></span></div>
      <div class="field"><span class="field-label">From:</span><span class="field-line"></span></div>
      <div class="field"><span class="field-label">Description:</span><span class="field-line"></span></div>
      <div class="field"><span class="field-label">Code:</span><span class="field-line"></span></div>
      <div class="field"><span class="field-label">Exp. Date</span><span class="field-line"></span></div>
    </section>

    <footer class="site-address">skyravelin.com.au</footer>
  </main>
</body>
</html>
```